Complete Stationery Package for Church
Wellspring
Modern
Pastor
417 Larkwood Rd. North Augusta, SC 29860
pastor@wellspringkv.org
wellspringkv.org
Service Schedule (Business Cards) Sunday a.m. 10 Sunday p.m. 6 Wed. p.m. 7:30 Visitor Cards should include the following: Welcome! Thank you for visiting with us! To help us become mor acquainted, please fill out the following information: Name, Date, Address, CIty, state, zip, Phone, email, Guest of ..., 3 check boxes that will include the following: 1) I would like more information about the New Testament plan of Salvation 2) I would like a free home BIble Study covering highlights of the Scriptures 3) I would like to share a special personal need with the Pastoral staff. Comments... Any questions just contact me and l look forwarding once again to working with you all! Stationary should include, but not limited to: Letterhead, envelopes, business cards, visitor card, folder, cd cover and sleeve, and email signature!
Church Info
maltby1983 maltby1983
Great looking designs so far! The pastor's name is Dale Harwick. Thanks
The stationary is for "Wellspring" church. You can use just Wellspring in the design process! Thanks and look forward to everyone's imagination!
rmvisions rmvisions
What church is the stationary being done for?

```html
<!DOCTYPE html>
<html lang="en">
<head>
<meta charset="utf-8">
<title>Wellspring — Stationery Package</title>
<link rel="stylesheet" href="https://fonts.googleapis.com/css2?family=Cinzel:wght@400;600&display=swap">
<style>
  :root {
    --ink: #111111;
    --gold: #c9a24a;
    --gray: #8c8c8c;
    --gray-light: #c8c8c8;
    --paper: #ffffff;
    --page: #ffffff;
    --text: #222222;
    --on-dark: #ffffff;
  }
  * { box-sizing: border-box; margin: 0; padding: 0; }
  html, body { width: 1200px; height: 864px; overflow: hidden; background: var(--page); }
  body { position: relative; font-family: "Cinzel", serif; color: var(--text); }

  .piece { position: absolute; background: var(--paper); box-shadow: 2px 3px 8px rgba(0,0,0,.25); overflow: hidden; }

  /* name lockup: one plain circle plus the name in body type */
  .brand { display: flex; align-items: center; gap: 10px; }
  .brand-dot { border-radius: 50%; background: var(--gold); flex: none; }
  .brand-name { font-family: "Cinzel", serif; font-weight: 400; line-height: 1; white-space: nowrap; color: var(--on-dark); letter-spacing: .02em; }
  .brand.on-light .brand-name { color: var(--text); }

  .social { display: flex; gap: 4px; }
  .social span { display: block; background: var(--gray); border-radius: 2px; }

  /* letterhead */
  .letterhead { left: 10px; top: 38px; width: 550px; height: 562px; }
  .letterhead .header { position: absolute; left: 0; top: 0; width: 100%; height: 100px; background: var(--ink); padding: 0 0 0 30px; display: flex; align-items: center; }
  .letterhead .stripe-gold { position: absolute; left: 20px; top: 100px; width: 9px; height: 430px; background: var(--gold); }
  .letterhead .stripe-gray { position: absolute; left: 29px; top: 100px; width: 7px; height: 430px; background: var(--gray-light); }
  .letterhead .footer { position: absolute; left: 0; bottom: 0; width: 100%; height: 32px; background: var(--ink); color: var(--on-dark); font-size: 9px; letter-spacing: .06em; display: flex; align-items: center; justify-content: center; gap: 14px; }

  /* envelope */
  .envelope { left: 155px; top: 300px; width: 532px; height: 212px; }
  .envelope .header { position: absolute; left: 0; top: 0; width: 100%; height: 70px; background: var(--ink); padding: 12px 0 0 18px; border-bottom: 4px solid var(--gold); }
  .envelope .address { color: var(--on-dark); font-size: 7px; letter-spacing: .06em; margin-top: 6px; }

  /* visitor card */
  .visitor { left: 668px; top: 30px; width: 512px; height: 282px; }
  .visitor .header { height: 52px; background: var(--ink); padding: 0 0 0 14px; border-bottom: 3px solid var(--gold); display: flex; align-items: center; }
  .visitor h2 { text-align: center; font-size: 15px; font-weight: 600; margin: 12px 0 6px; letter-spacing: .04em; }
  .visitor .intro { text-align: center; font-size: 7.5px; letter-spacing: .04em; margin-bottom: 10px; }
  .form { padding: 0 34px; font-size: 8px; letter-spacing: .05em; }
  .row { display: flex; align-items: flex-end; gap: 6px; margin-bottom: 11px; }
  .row .line { flex: 1; border-bottom: 1px solid #555; height: 1px; }
  .checks { margin-top: 4px; }
  .check { display: flex; align-items: center; gap: 6px; font-size: 6.5px; margin-bottom: 3px; }
  .check i { width: 7px; height: 7px; border: 1px solid #333; flex: none; }

  /* cd */
  .disc { position: absolute; left: 950px; top: 373px; width: 204px; height: 204px; }
  .sleeve { left: 720px; top: 350px; width: 236px; height: 238px; background: var(--gray-light); }
  .sleeve .band { position: absolute; left: 0; top: 128px; width: 100%; height: 50px; background: var(--ink); border-top: 3px solid var(--gold); border-bottom: 3px solid var(--gold); padding: 0 0 0 16px; display: flex; align-items: center; }

  /* business cards */
  .card-front { left: 220px; top: 638px; width: 425px; height: 187px; background: var(--ink); display: flex; align-items: center; justify-content: center; }
  .card-back { left: 670px; top: 638px; width: 505px; height: 187px; }
  .card-back .logo { position: absolute; left: 12px; top: 16px; }
  .card-back .name { position: absolute; left: 16px; top: 96px; font-size: 15px; font-weight: 600; letter-spacing: .03em; }
  .card-back .schedule { position: absolute; right: 18px; top: 14px; text-align: right; font-size: 10px; line-height: 1.35; letter-spacing: .04em; }
  .card-back .schedule h3 { font-size: 15px; font-weight: 400; margin-bottom: 2px; }
  .card-back .contact { position: absolute; right: 18px; top: 100px; text-align: right; font-size: 9px; line-height: 1.4; letter-spacing: .04em; }
  .card-back .social { position: absolute; left: 16px; top: 138px; }
  .card-back .web { position: absolute; left: 16px; bottom: 10px; font-size: 8.5px; letter-spacing: .04em; }
  .card-back .email { position: absolute; right: 18px; bottom: 10px; font-size: 8.5px; letter-spacing: .04em; }
</style>
</head>
<body>

<section class="piece letterhead">
  <div class="header">
    <div class="brand">
      <span class="brand-dot" style="width:44px;height:44px"></span>
      <span class="brand-name" style="font-size:32px">Wellspring</span>
    </div>
  </div>
  <div class="stripe-gold"></div>
  <div class="stripe-gray"></div>
  <div class="footer">
    <span>417 Larkwood Rd. North Augusta, SC 29860</span>
    <span>Phone: 919-555-0142</span>
    <div class="social"><span style="width:10px;height:10px"></span><span style="width:10px;height:10px"></span><span style="width:10px;height:10px"></span></div>
    <span>wellspringkv.org</span>
  </div>
</section>

<section class="piece envelope">
  <div class="header">
    <div class="brand">
      <span class="brand-dot" style="width:26px;height:26px"></span>
      <span class="brand-name" style="font-size:20px">Wellspring</span>
    </div>
    <p class="address">417 Larkwood Rd. North Augusta, SC 29860</p>
  </div>
</section>

<section class="piece visitor">
  <div class="header">
    <div class="brand">
      <span class="brand-dot" style="width:30px;height:30px"></span>
      <span class="brand-name" style="font-size:21px">Wellspring</span>
    </div>
  </div>
  <h2>Welcome! Thank you for visiting with us!</h2>
  <p class="intro">To help us become more acquainted, please fill out the following information:</p>
  <div class="form">
    <div class="row"><span>Name</span><span class="line"></span><span>Date</span><span class="line" style="flex:.4"></span></div>
    <div class="row"><span>Address</span><span class="line"></span></div>
    <div class="row"><span>City</span><span class="line"></span><span>State</span><span class="line" style="flex:.4"></span><span>Zip</span><span class="line" style="flex:.4"></span></div>
    <div class="row"><span>Guest of</span><span class="line"></span></div>
    <div class="checks">
      <div class="check"><i></i>I would like more information about the New Testament plan of Salvation</div>
      <div class="check"><i></i>I would like a free home Bible Study covering highlights of the Scriptures</div>
      <div class="check"><i></i>I would like to share a special personal need with the Pastoral staff</div>
    </div>
  </div>
</section>

<svg class="disc" viewBox="0 0 204 204" aria-hidden="true">
  <circle cx="102" cy="102" r="100" fill="#111"/>
  <circle cx="102" cy="102" r="46" fill="#9a9a9a"/>
  <circle cx="102" cy="102" r="12" fill="#ffffff"/>
</svg>
<section class="piece sleeve">
  <div class="band">
    <div class="brand">
      <span class="brand-dot" style="width:24px;height:24px"></span>
      <span class="brand-name" style="font-size:17px">Wellspring</span>
    </div>
  </div>
</section>

<section class="piece card-front">
  <div class="brand">
    <span class="brand-dot" style="width:50px;height:50px"></span>
    <span class="brand-name" style="font-size:36px">Wellspring</span>
  </div>
</section>

<section class="piece card-back">
  <div class="brand on-light logo">
    <span class="brand-dot" style="width:34px;height:34px"></span>
    <span class="brand-name" style="font-size:24px">Wellspring</span>
  </div>
  <p class="name">Pastor Dale Harwick</p>
  <div class="schedule">
    <h3>Service Schedule</h3>
    <p>Sunday A.M. 10</p>
    <p>Sunday P.M. 6</p>
    <p>Wed. P.M. 7:30</p>
  </div>
  <div class="contact">
    <p>417 Larkwood Road</p>
    <p>North Augusta, S.C. 29860</p>
    <p>Phone: 919-555-0142</p>
    <p>Cell: 919-555-0187</p>
  </div>
  <div class="social"><span style="width:14px;height:14px"></span><span style="width:14px;height:14px"></span><span style="width:14px;height:14px"></span></div>
  <p class="web">wellspringkv.org</p>
  <p class="email">Email: pastor@wellspringkv.org</p>
</section>

</body>
</html>
```